price list for web and print- sending to inquiring clients and use as promo material

Hello
I need a graphic design for my photography price list/s. I am a people photographer. The first of 6 price sheets will be for head shots- I would like a price sheet that captures the prospective clients' attention. The info and visual should be compelling and easy to digest. It should be simple yet interesting. I will provide you with some pictures but you do not have to include them. I have a studio indoors and outdoors also working on location. This design should be for email and print. The picture of "ingrid" is me and I use that on all my profiles. I like the fonts in the logo but it is too boxy and rigid

Target Market(s)

repeat client, word of mouth referrals, new people but aquaintances of others that might know me

Industry/Entity Type

Graphic Design

Font styles to use
Serif
Sans Serif
Script

Requirements
Must have
• prices and maybe some words about my services that I sent in... Please tie it together as best as possible..
Nice to have
• Loosen up my logo.. it is in a box.....contemporary design but not something that would not fit in with corporate.. I like this headline
• "Create a great first impression with your professional headshots"
• I sent in other copy and my logo(sent in the picture drop box)

```html
<!DOCTYPE html>
<html lang="en">
<head>
<meta charset="utf-8">
<title>Ingrid M. Hale Photography – Headshot Packages</title>
<link rel="stylesheet" href="https://fonts.googleapis.com/css2?family=Dancing+Script:wght@600&family=Lato:wght@400;700&family=Oswald:wght@600&display=swap">
<style>
  :root {
    --ink: #0c0c0c;
    --red: #e01b1b;
    --red-deep: #b50f12;
    --white: #ffffff;
    --paper: #f6f9fc;
    --body: #333333;
    --stage: #ece8e2;
  }
  * { box-sizing: border-box; margin: 0; padding: 0; }
  html, body { width: 907px; height: 1200px; overflow: hidden; background: var(--stage); }
  .canvas { position: relative; width: 907px; height: 1200px; font-family: 'Lato', sans-serif; }
  .sheet { position: absolute; left: 100px; top: 103px; width: 710px; height: 995px; overflow: hidden; background: var(--paper); }
  .shapes { position: absolute; left: -100px; top: -103px; width: 907px; height: 1200px; }
  .pos { position: absolute; }
  h1, h2, h3 { font-weight: 400; }

  .brand { left: 0; top: 44px; width: 205px; text-align: center; color: var(--white); font-weight: 700; }
  .brand__name { font-size: 24px; line-height: 1; }
  .brand__rule { width: 136px; height: 1px; background: var(--white); margin: 7px auto 5px; }
  .brand__sub { font-size: 11px; letter-spacing: 3px; }

  .headline__script { left: 18px; top: 308px; font-family: 'Dancing Script', cursive; font-weight: 600; color: var(--ink); font-size: 34px; line-height: 40px; white-space: nowrap; transform: scaleX(0.74); transform-origin: left center; }
  .headline__main { left: 18px; top: 360px; color: var(--white); font-size: 24px; line-height: 32px; white-space: nowrap; }

  .feature-tag { color: var(--white); font-size: 21px; height: 33px; line-height: 33px; padding-left: 14px; background: var(--ink); border-radius: 0 17px 17px 0; }
  .feature-text { left: 10px; width: 280px; font-size: 11px; line-height: 14px; color: var(--body); text-align: justify; }

  .phone { left: 44px; top: 938px; display: flex; align-items: center; gap: 14px; color: var(--white); font-size: 21px; letter-spacing: 0.5px; }

  .packages__title { right: 23px; top: 163px; text-align: right; font-size: 31px; line-height: 40px; }
  .packages__title .accent { color: var(--red); }
  .packages__title .plain { color: var(--white); }

  .pkg-tag { right: 0; height: 31px; line-height: 31px; padding: 0 23px 0 18px; background: var(--white); color: var(--ink); font-size: 16px; border-radius: 16px 0 0 16px; }
  .pkg-sub { right: 20px; color: var(--white); font-weight: 700; font-style: italic; font-size: 16px; text-align: right; line-height: 20px; }
  .pkg-list { right: 24px; list-style: none; color: var(--white); font-size: 11px; text-align: right; }
  .pkg-list li { position: relative; padding-right: 29px; line-height: 21px; }
  .pkg-list li::after { content: ""; position: absolute; right: 0; top: 7px; width: 7px; height: 7px; border-radius: 50%; background: var(--red); }
  .pkg-list--tight li { line-height: 13px; margin-bottom: 8px; }

  .price { width: 179px; height: 51px; background: var(--red); border-radius: 6px; text-align: center; color: var(--white); font-family: 'Oswald', sans-serif; }
  .price__amount { font-size: 17px; line-height: 22px; padding-top: 4px; }
  .price__extra { font-size: 10px; line-height: 14px; }

  .location { right: 24px; top: 846px; width: 370px; color: var(--white); font-size: 10px; line-height: 12px; text-align: right; }
  .location p { margin-bottom: 6px; }
  .location .dot { position: absolute; right: -3px; top: -6px; width: 7px; height: 7px; border-radius: 50%; background: var(--red); }
</style>
</head>
<body>
<main class="canvas">
  <section class="sheet" aria-label="Headshot price list">
    <svg class="shapes" viewBox="0 0 907 1200">
      <defs>
        <linearGradient id="lens" x1="0" y1="0" x2="1" y2="1">
          <stop offset="0" stop-color="#e8c09a"/>
          <stop offset="0.35" stop-color="#8a3a4a"/>
          <stop offset="0.7" stop-color="#3a1d2e"/>
          <stop offset="1" stop-color="#c25a52"/>
        </linearGradient>
        <linearGradient id="band" x1="0" y1="0" x2="1" y2="0">
          <stop offset="0" stop-color="#b31015"/>
          <stop offset="1" stop-color="#e6201c"/>
        </linearGradient>
        <linearGradient id="wash" x1="0" y1="0" x2="1" y2="1">
          <stop offset="0" stop-color="#ffffff"/>
          <stop offset="0.5" stop-color="#e4eef8"/>
          <stop offset="1" stop-color="#ffffff"/>
        </linearGradient>
      </defs>
      <rect x="100" y="537" width="360" height="420" fill="url(#wash)"/>
      <rect x="100" y="103" width="710" height="300" fill="url(#lens)" role="img" aria-label="Photo: close-up of a camera lens with soft warm bokeh"/>
      <path d="M100 103 H305 V205 L215 263 L100 205 Z" fill="var(--ink)"/>
      <rect x="100" y="397" width="332" height="140" fill="url(#band)"/>
      <path d="M100 940 Q 330 1040 810 1072 V1098 H100 Z" fill="url(#band)"/>
      <path d="M810 225 C 660 225 525 290 466 372 Q 440 410 440 460 V1060 Q 620 1078 810 1066 Z" fill="var(--ink)" stroke="var(--white)" stroke-width="6"/>
    </svg>

    <div class="pos brand">
      <div class="brand__name">Ingrid M. Hale</div>
      <div class="brand__rule"></div>
      <div class="brand__sub">PHOTOGRAPHY</div>
    </div>

    <h1>
      <span class="pos headline__script">Create a great first impression</span>
      <span class="pos headline__main">WITH YOUR PROFESSIONAL<br>HEADSHOTS</span>
    </h1>

    <h2 class="pos feature-tag" style="top:452px;width:133px;">Expereienc</h2>
    <p class="pos feature-text" style="top:500px;">Ingrid is an accomplished professional photographer who has helped thousands of clients. She is an expert at helping you look confident and approachable.</p>

    <h2 class="pos feature-tag" style="top:571px;width:230px;">24 Hour Turnaround</h2>
    <p class="pos feature-text" style="top:622px;">Your time is valuable. Ingrid can complete the photoshoot in just 30 minutes. (Or as long as you want.) Our process is designed to save you time.</p>

    <h2 class="pos feature-tag" style="top:694px;width:133px;">Enjoyable</h2>
    <p class="pos feature-text" style="top:748px;">You can look forward to an enjoyable photo session with Ingrid's professional guidance. Ingrid helps make the experience fun.</p>

    <div class="pos phone">
      <svg width="36" height="34" viewBox="0 0 36 34" aria-hidden="true">
        <path d="M6 4 L12 3 L15 11 L11 14 Q14 21 20 24 L23 20 L31 23 L30 29 Q27 32 22 31 Q8 26 3 12 Q2 7 6 4 Z" fill="var(--ink)"/>
        <path d="M21 3 Q30 4 32 13 M21 8 Q26 9 27 13" stroke="var(--ink)" stroke-width="2" fill="none"/>
      </svg>
      <span>0123456789</span>
    </div>

    <h2 class="pos packages__title"><span class="accent">POPULAR</span><br><span class="plain">PACKAGES</span></h2>

    <h3 class="pos pkg-tag" style="top:257px;">ENTRY PACKAGE</h3>
    <p class="pos pkg-sub" style="top:300px;">Quick and Simple</p>
    <div class="pos price" style="left:347px;top:331px;"><div class="price__amount">Just $175</div><div class="price__extra">Additional images just $75 each</div></div>
    <ul class="pos pkg-list pkg-list--tight" style="top:329px;">
      <li>One pose</li><li>One wardrobe</li><li>One selected image<br>retouched</li>
    </ul>

    <h3 class="pos pkg-tag" style="top:416px;">2 POSE PACKAGE</h3>
    <p class="pos pkg-sub" style="top:462px;">Most Popular</p>
    <div class="pos price" style="left:347px;top:463px;"><div class="price__amount">just $175</div><div class="price__extra">Additional images just $75 each</div></div>
    <ul class="pos pkg-list" style="top:490px;">
      <li>Two poses</li><li>Two wardrobe changes</li><li>Two selected images retouched</li><li>One or two background changes</li>
    </ul>

    <h3 class="pos pkg-tag" style="top:583px;">PREMIER PACKAGE</h3>
    <p class="pos pkg-sub" style="top:622px;">Get it all<br>Most Popular</p>
    <div class="pos price" style="left:355px;top:630px;"><div class="price__amount">Just $525</div><div class="price__extra">Additional images just $75 each</div></div>
    <ul class="pos pkg-list" style="top:664px;">
      <li>Four poses</li><li>3-4 wardrobe changes</li><li>4 selected images retouched</li><li>2-3 background changes</li><li>Additional images just $75 each</li><li>Optional outdoor studio</li>
    </ul>

    <h3 class="pos pkg-tag" style="top:801px;">AT YOUR LOCATION</h3>
    <div class="pos location">
      <span class="dot"></span>
      <p>$250 set up charge, minimum of 5 people<br>one selected image retouched<br>each additional image $50 each</p>
      <p>If possible, we like ½ hour appts for each person so they can view their<br>images on the computer<br>5-10 people $150 EACH<br>11-20 people $100 each<br>20+ $75 each</p>
    </div>
  </section>
</main>
</body>
</html>
```